Lattiro.com home page upgrade. Strong existing assets.

We are looking to redesign our homepage. We need to communicate three large concepts.

1) Software-as-a-Service for connected electronic device management
2) Mesh-Networking-as-a-Service allows local devices to talk together easily
3) We have 3 pieces of hardware:
A) K7 Beetle
B) K7 Moth
C) K7 Grasshopper

We will keep the color scheme, although we would like the general feel to be lighter than our current page at http://lattiro.com

See the word doc for more details.

Closing soon! Get in last designs! 

Industry/Entity Type

Electronic

Requirements
Nice to have
• large images, modern design

```html
<!DOCTYPE html>
<html lang="en">
<head>
<meta charset="utf-8">
<title>Lattiro — Internet-of-Things Solutions</title>
<link rel="stylesheet" href="https://fonts.googleapis.com/css2?family=Oswald:wght@400;500;600&family=Roboto:wght@400;500;700&display=swap">
<style>
:root{
  --plum:#4b2a33;
  --plum-deep:#3d2229;
  --orange:#e8862a;
  --orange-dark:#d4731c;
  --paper:#eef0f1;
  --white:#ffffff;
  --ink:#2e2a2b;
  --muted:#5a5556;
  --grey-band:#5e5c5d;
}
*{box-sizing:border-box;margin:0;padding:0}
html,body{width:721px;height:1200px;overflow:hidden}
body{font-family:"Roboto",Arial,sans-serif;color:var(--ink);background:var(--white);position:relative}
.heading{font-family:"Oswald","Arial Narrow",sans-serif;font-weight:400}

.top-bar{height:16px;background:var(--plum);display:flex;justify-content:space-between;align-items:center;padding:0 149px 0 156px}
.social{display:flex;gap:3px}
.social span{width:10px;height:10px;border-radius:50%;background:var(--white)}
.phone{display:flex;align-items:center;gap:4px;color:var(--white);font-size:8px;font-weight:700;letter-spacing:.3px}

.site-header{height:45px;display:flex;align-items:center;padding:0 0 0 156px;border-bottom:1px solid #ddd}
.brand{font-family:"Oswald",sans-serif;font-weight:600;font-size:28px;color:var(--plum);width:148px}
.main-nav{display:flex;margin-left:0}
.main-nav a{font-family:"Oswald",sans-serif;font-size:7.5px;color:var(--muted);text-decoration:none;text-align:center;line-height:1.15;width:48px;padding:9px 0}
.main-nav a.active{color:var(--plum);border-bottom:2px solid var(--plum)}

.hero{position:relative;height:288px;background:radial-gradient(ellipse at 45% 40%,#f0c878 0%,#b88a3a 35%,#6a4a22 70%,#3b2a14 100%);overflow:hidden}
.hero-devices{position:absolute;left:118px;top:44px;width:253px;height:212px;border-radius:10px;background:linear-gradient(160deg,#2a2a2a,#0f0f0f);box-shadow:0 6px 14px rgba(0,0,0,.45)}
.hero-copy{position:absolute;left:381px;top:63px}
.hero-title{font-family:"Oswald",sans-serif;font-weight:500;font-size:28px;line-height:33px;color:var(--white);text-shadow:1px 2px 2px rgba(0,0,0,.55)}
.hero-tag{margin-top:10px;width:184px;background:var(--orange);padding:3px 4px;font-size:13.5px;font-weight:500;line-height:16.5px;color:#2b1a10}
.slider-dots{position:absolute;left:513px;top:274px;display:flex;gap:3px}
.slider-dots span{width:10px;height:10px;background:var(--orange);border:1px solid #fff}
.slider-dots span.on{background:var(--white)}

.welcome{height:139px;background:var(--paper);text-align:center;padding-top:18px}
.welcome h2{font-size:16px;color:var(--ink)}
.welcome h2 b,.why h2 b{font-weight:600}
.divider{display:flex;align-items:center;justify-content:center;gap:6px;margin:10px auto 12px;width:378px}
.divider i{flex:1;height:2px;background:#cfd2d3}
.divider em{font-family:"Oswald",sans-serif;color:#b8b8b8;font-size:12px;line-height:8px}
.welcome p{font-size:6.4px;line-height:9.5px;color:var(--muted);width:380px;margin:0 auto 6px}

.why{height:192px;background:var(--plum);text-align:center;padding-top:16px;color:var(--white)}
.why h2{font-size:16px}
.why-grid{display:flex;justify-content:center;margin-top:18px}
.why-item{width:139px;position:relative}
.why-item + .why-item::before{content:"";position:absolute;left:0;top:6px;width:2px;height:100px;background:linear-gradient(transparent,#2a151a,transparent)}
.why-icon{width:51px;height:51px;border-radius:50%;background:var(--orange);margin:0 auto;display:flex;align-items:center;justify-content:center}
.why-item h3{font-family:"Oswald",sans-serif;font-weight:400;color:var(--orange);font-size:9px;line-height:11.5px;margin-top:13px}
.why-item p{font-size:6px;line-height:7.5px;margin-top:4px}

.services{height:220px;background:var(--paper);text-align:center;padding-top:18px}
.services h2{font-family:"Oswald",sans-serif;font-weight:400;color:var(--orange);font-size:14.5px;line-height:18px}
.services p{font-size:6.4px;line-height:12px;color:var(--ink)}
.services p.tight{line-height:8px;width:380px;margin:0 auto 3px}
.cta{display:inline-block;background:var(--plum);color:var(--white);font-size:6.4px;font-weight:700;padding:3px 12px;border-radius:2px;margin:2px 0 12px}

.advantages{height:182px;text-align:center;padding-top:22px}
.advantages h2{font-size:14.5px;color:var(--ink);font-weight:500}
.adv-grid{display:flex;justify-content:center;gap:56px;margin-top:18px}
.adv-item{width:88px}
.adv-screen{height:65px;border:2px solid #d5d5d5;background:var(--plum);display:flex;align-items:center;justify-content:center;box-shadow:0 3px 4px rgba(0,0,0,.25)}
.adv-disc{width:38px;height:38px;border-radius:50%;background:#6b3f49;display:flex;align-items:center;justify-content:center}
.adv-item h3{font-family:"Oswald",sans-serif;font-weight:400;color:var(--orange);font-size:11px;margin-top:10px}

.signup{height:36px;background:var(--grey-band);display:flex;align-items:center;padding-left:156px}
.signup-label{height:36px;width:66px;background:#ececec;font-family:"Oswald",sans-serif;font-size:10.5px;color:var(--ink);display:flex;align-items:center;justify-content:center;position:relative}
.signup-label::after{content:"";position:absolute;right:-18px;top:0;border-left:18px solid #ececec;border-top:18px solid transparent;border-bottom:18px solid transparent}
.signup-text{font-size:6.4px;line-height:8px;color:var(--white);margin-left:26px;width:108px}
.signup input{height:15px;width:82px;margin-left:5px;border:1px solid #ccc;font-size:6.5px;padding:0 4px;font-family:"Roboto",sans-serif}
.signup button{height:15px;margin-left:5px;padding:0 4px;font-size:7px;font-weight:700;border:1px solid #bbb;background:#e6e6e6;color:var(--ink)}

.site-footer{height:82px;background:var(--plum-deep);text-align:center;padding-top:10px}
.site-footer .brand{width:auto;color:var(--white);font-size:26px;line-height:30px}
.footer-nav{margin-top:4px}
.footer-nav a{font-family:"Oswald",sans-serif;color:var(--orange);font-size:6.5px;text-decoration:none;margin:0 2px}
.copyright{font-family:"Oswald",sans-serif;color:var(--orange-dark);font-size:5.5px;margin-top:6px}
</style>
</head>
<body>

<div class="top-bar">
  <div class="social"><span></span><span></span><span></span></div>
  <div class="phone">
    <svg width="8" height="8" viewBox="0 0 24 24"><path fill="#e8862a" d="M6.6 10.8a15.1 15.1 0 006.6 6.6l2.2-2.2c.3-.3.7-.4 1-.2 1.1.4 2.3.6 3.6.6.6 0 1 .4 1 1V20c0 .6-.4 1-1 1A17 17 0 013 4c0-.6.4-1 1-1h3.5c.6 0 1 .4 1 1 0 1.3.2 2.5.6 3.6.1.3 0 .7-.2 1z"/></svg>
    555-014-2290
  </div>
</div>

<header class="site-header">
  <div class="brand">Lattiro</div>
  <nav class="main-nav">
    <a href="#">Manufacturers</a>
    <a href="#" class="active">Technology<br>Integrators</a>
    <a href="#">Enterprise<br>Plans</a>
    <a href="#">K7<br>Devices</a>
    <a href="#">About<br>Us</a>
    <a href="#">Contact<br>Us</a>
  </nav>
</header>

<section class="hero">
  <div class="hero-devices" role="img" aria-label="Tablet and smartphones showing the Lattiro dashboard"></div>
  <div class="hero-copy">
    <h1 class="hero-title">Your Professional<br>"Internet-of-Things"<br>Solution-Today</h1>
    <p class="hero-tag">Scalable, Secure,<br>Full-stack M2M Solution<br>On Web &amp; Mobile</p>
  </div>
  <div class="slider-dots"><span class="on"></span><span></span><span></span><span></span></div>
</section>

<section class="welcome">
  <h2 class="heading">Welcome to <b>Lattiro</b></h2>
  <div class="divider"><i></i><em>"</em><i></i></div>
  <p>Lorem ipsum dolor sit amet, consectetuer adipiscing elit, sed diam nonummy nibh euismod tincidunt ut laoreet dolore magna aliquam erat volutpat. Ut wisi enim ad minim veniam, quis nostrud exerci tation ullamcorper suscipit lobortis nisl ut aliquip ex<br>Duis autem vel eum iriure dolor in hendrerit in vulputate velit esse molestie consequat, vel illum</p>
  <p>Lorem ipsum dolor sit amet, consectetuer adipiscing elit, sed diam nonummy nibh euismod tincidunt ut laoreet dolore magna erat volutpat. Ut wisi enim ad minim veniam, quis nostrud exerci tation ullamcorper suscipit lobortis</p>
</section>

<section class="why">
  <h2 class="heading">Why choose <b>Lattiro</b></h2>
  <div class="why-grid">
    <div class="why-item">
      <div class="why-icon"><svg width="28" height="28" viewBox="0 0 24 24" fill="none" stroke="#fff" stroke-width="2.2" stroke-linecap="round"><path d="M4 20L13 4M20 20L11 4M6 15h12"/></svg></div>
      <h3>Lattiro For<br>OEM's</h3>
      <p>New Revenue! Add a Web and Mobile<br>M2M Product-Line with Lattiro</p>
    </div>
    <div class="why-item">
      <div class="why-icon"><svg width="30" height="30" viewBox="0 0 24 24" fill="none" stroke="#fff" stroke-width="1.6"><circle cx="12" cy="12" r="9"/><ellipse cx="12" cy="12" rx="4" ry="9"/><path d="M3 12h18M5 7h14M5 17h14"/></svg></div>
      <h3>Lattiro For<br>Technology Integrators</h3>
      <p>Enhance Your Service Offering with<br>Connected Devices!</p>
    </div>
    <div class="why-item">
      <div class="why-icon"><svg width="30" height="28" viewBox="0 0 24 22" fill="#fff"><rect x="2" y="2" width="8" height="19"/><rect x="11" y="8" width="11" height="13"/><g fill="#e8862a"><rect x="4" y="5" width="4" height="1.5"/><rect x="4" y="9" width="4" height="1.5"/><rect x="4" y="13" width="4" height="1.5"/><rect x="13" y="11" width="3" height="2"/><rect x="17.5" y="11" width="3" height="2"/><rect x="13" y="15" width="3" height="2"/><rect x="17.5" y="15" width="3" height="2"/></g></svg></div>
      <h3>Lattiro Enterprise Plans For<br>Companies</h3>
      <p>Quickly get a solution running that<br>ties to your back office</p>
    </div>
  </div>
</section>

<section class="services">
  <h2>SOFTWARE-AS-A-SERVICE</h2>
  <p>• Lattiro Solutions require no IT infrastructure or overhead</p>
  <a class="cta" href="#">Unless you want it to? &nbsp;Click here for Enterprise Plans.</a>
  <h2>HARDWARE SERVICE</h2>
  <p class="tight">• The <b>K7 Beetle</b> from Lattiro connects your devices to the Internet-to-Things</p>
  <p class="tight">• The <b>K7 Moth</b> connects over mesh network to the K7 Beetle, it doesn't connect to the internet directly.</p>
  <p class="tight">• The <b>K7 Grasshopper</b> Connects to the internet has the 2 relays, 2 Digital I/O's, and 2 serial ports but does not create a mesh network. &nbsp;It is a stand-alone device.</p>
  <a class="cta" href="#">Have your own hardware? No problem! Click Here" AND Learn More</a>
  <h2>MESH-NETWORKING-AS-A-SERVICE</h2>
  <p>•Local devices can be meshed together seamlessly</p>
</section>

<section class="advantages">
  <h2 class="heading">Lattiro Advantages</h2>
  <div class="adv-grid">
    <div class="adv-item">
      <div class="adv-screen"><div class="adv-disc"><svg width="24" height="18" viewBox="0 0 24 18"><path fill="#fff" d="M19 7a6 6 0 00-11.6-1.5A4.5 4.5 0 005 14h14a3.5 3.5 0 000-7z"/><path fill="#6b3f49" d="M12 6l4 4h-2.5v4h-3v-4H8z"/></svg></div></div>
      <h3>CLOUD MANAGED</h3>
    </div>
    <div class="adv-item">
      <div class="adv-screen"><div class="adv-disc"><svg width="12" height="22" viewBox="0 0 12 22"><rect x="0.5" y="0.5" width="11" height="21" rx="2" fill="#fff"/><rect x="2" y="3" width="8" height="14" fill="#6b3f49"/><circle cx="6" cy="19.2" r="1" fill="#6b3f49"/></svg></div></div>
      <h3>APPS</h3>
    </div>
    <div class="adv-item">
      <div class="adv-screen"><div class="adv-disc"><svg width="24" height="24" viewBox="0 0 24 24"><path fill="#fff" d="M10 1h4l.6 3 2.2 1 2.6-1.7 2.8 2.8L20.5 8.7l1 2.3 3 .6v4l-3 .6-1 2.2 1.7 2.6-2.8 2.8-2.6-1.7-2.2 1-.6 3h-4l-.6-3-2.3-1-2.6 1.7-2.8-2.8 1.7-2.6-1-2.2-3-.6v-4l3-.6 1-2.3L1.7 6.1l2.8-2.8L7.1 5l2.3-1z" transform="scale(.92) translate(1 1)"/><circle cx="12" cy="12" r="4" fill="#6b3f49"/></svg></div></div>
      <h3>INTERNET SECURITY</h3>
    </div>
  </div>
</section>

<section class="signup">
  <div class="signup-label">EMAIL SIGNUP</div>
  <p class="signup-text">Stay connected and receive email updates from Lattiro.</p>
  <input type="text" placeholder="Name">
  <input type="email" placeholder="Email">
  <button type="button">SUBMIT</button>
</section>

<footer class="site-footer">
  <div class="brand">Lattiro</div>
  <nav class="footer-nav">
    <a href="#">Manufacturers</a><a href="#">Technology Integrators</a><a href="#">Enterprise Plans</a><a href="#">K7 Devices</a><a href="#">About Us</a><a href="#">Contact Us</a>
  </nav>
  <p class="copyright">© 2014 Lattiro. All Rights Reserved.</p>
</footer>

</body>
</html>
```